Marwick Law Letterhead

We need a new letterhead design for a Law Firm. The address for the law firm is 4175 Calloway Avenue, Suite 200, Houston, Texas 77046. Phone Number: 832-614-2093; Fax Number: 832-307-1546. The logo is uploaded to the project.

```html
<!DOCTYPE html>
<html lang="en">
<head>
<meta charset="UTF-8">
<title>Marwick Law Letterhead</title>
<link rel="stylesheet" href="https://fonts.googleapis.com/css2?family=Montserrat:wght@400;500;600&display=swap">
<style>
  :root {
    --backdrop: #e9e9ec;
    --paper: #ffffff;
    --ink: #1b1b1b;
    --navy: #1f2f5e;
    --red: #e31b23;
    --red-deep: #6b0010;
    --rule: #b3121c;
  }
  * { box-sizing: border-box; margin: 0; padding: 0; }
  html, body {
    width: 1200px; height: 960px; overflow: hidden;
    background: var(--backdrop);
    font-family: "Montserrat", sans-serif;
    color: var(--ink);
  }
  .letterhead {
    position: absolute; left: 282px; top: 28px;
    width: 636px; height: 904px;
    background: var(--paper);
    box-shadow: 0 10px 30px rgba(0,0,0,.12);
    overflow: hidden;
  }
  .band {
    position: absolute; left: 0; width: 100%;
    background: linear-gradient(90deg, var(--red) 0%, var(--red) 45%, var(--red-deep) 100%);
  }
  .band--top { top: 0; height: 12px; }
  .band--bottom { bottom: 0; height: 24px; }
  .masthead {
    position: absolute; top: 42px; left: 48px; right: 44px;
    display: flex; justify-content: space-between; align-items: flex-start;
  }
  .brand {
    display: flex; align-items: center; gap: 10px;
    margin-top: 38px;
  }
  .brand__mark {
    width: 26px; height: 26px; border-radius: 50%;
    background: var(--navy);
  }
  .brand__name {
    font-size: 26px; font-weight: 500; color: var(--navy);
    letter-spacing: .5px;
  }
  .contact {
    display: flex; gap: 12px;
    font-size: 9.5px; line-height: 1.45;
  }
  .contact__rule { width: 1px; background: var(--rule); align-self: stretch; }
  .contact__line { display: flex; align-items: center; gap: 6px; }
  .contact__line svg { width: 9px; height: 9px; fill: var(--red); }
  .letter {
    position: absolute; top: 168px; left: 64px; right: 64px;
    font-size: 10.5px; line-height: 1.6;
  }
  .recipient { margin-bottom: 2px; }
  .letter p { margin-bottom: 16px; }
  .closing { margin-top: 6px; font-size: 11px; }
  .signature {
    margin-top: 8px; width: 110px; height: 30px;
    background: linear-gradient(90deg, #2a2a2a 0%, #5a5a5a 100%);
    opacity: .18; border-radius: 3px;
  }
</style>
</head>
<body>
  <main class="letterhead">
    <div class="band band--top"></div>

    <header class="masthead">
      <div class="brand">
        <span class="brand__mark"></span>
        <span class="brand__name">Marwick Law</span>
      </div>
      <div class="contact">
        <span class="contact__rule"></span>
        <div>
          <div>4175 Calloway Avenue,</div>
          <div>Suite 200, Houston,</div>
          <div>Texas 77046</div>
          <div class="contact__line">
            <svg viewBox="0 0 24 24"><path d="M6.6 10.8a15.1 15.1 0 0 0 6.6 6.6l2.2-2.2a1 1 0 0 1 1-.25 11.4 11.4 0 0 0 3.6.57 1 1 0 0 1 1 1V20a1 1 0 0 1-1 1A17 17 0 0 1 3 4a1 1 0 0 1 1-1h3.5a1 1 0 0 1 1 1c0 1.25.2 2.45.57 3.6a1 1 0 0 1-.25 1z"/></svg>
            <span>832-614-2093</span>
          </div>
          <div class="contact__line">
            <svg viewBox="0 0 24 24"><path d="M6 3h12v5H6zM4 9h16a2 2 0 0 1 2 2v6h-4v4H6v-4H2v-6a2 2 0 0 1 2-2zm4 7v3h8v-3z"/></svg>
            <span>832-307-1546</span>
          </div>
        </div>
      </div>
    </header>

    <section class="letter">
      <div class="recipient">Mr/s<br>First Name and Last Name<br>Company Name<br>Address</div>
      <p>Lorem ipsum dolor sit amet,consectetur adipiscing sed do eiusmod tempor incididunt laboreet dolore magna aliqua.Ut enim ad minim.veniam, quis nostrud exercitation ullamco laboris nisi ut aliquip exea commodo consequat.Lorem ipsum dolor sit amet,consectetur adipiscing sed do eiusmod tempor incididunt.labore et dolore magna aliqua. Ut enim</p>
      <p>Lorem ipsum dolor sit amet, consectetur adipiscing sed do eiusmod tempor incididunt labore et dolore magna aliqua. Ut enim ad minim veniam, quis nostrud exercitation ullamco laboris nisi ut aliquip exea commodo consequat.Duis aute irure dolor in reprehenderit in voluptate velit esse cillum irure dolor in reprehenderit in voluptate velit esse irure</p>
      <p>Lorem ipsum dolor sit amet, consectetur adipiscing sed do eiusmod tempor incididunt labore et dolore magna aliqua. consequat. Duis aute irure dolor in.reprehenderit in voluptate velit esse cillum dolore eu fugiat nulla pariatur. Excepteur sint occaecat cupidatat non proident, sunt in culpa qui officia deserunt mollit,</p>
      <p>Lorem ipsum dolor sit amet, consectetur adipiscing sed do eiusmod tempor incididunt labore et dolore magna aliqua. Ut enim Lorem ipsum dolor sit amet, consectetur adipiscing sed do eiusmod tempor incididunt labore et dolore magna aliqua. Ut enim Lorem ipsum aliqua.ipsum</p>
      <p>Lorem ipsum dolor sit amet, consectetur adipiscing sed do eiusmod tempor incididunt labore et dolore magna aliqua. Ut enim ad minim veniam, quis nostrud exercitation ullamco laboris nisi ut aliquip exea commodo consequat.Duis aute irure dolor in reprehenderit in voluptate velit esse cillum irure dolor in reprehenderit in voluptate velit esse irure</p>
      <p>Lorem ipsum dolor sit amet, consectetur adipiscing sed do eiusmod tempor incididunt labore et dolore magna aliqua. Ut enim ad minim veniam, quis nostrud exercitation ullamco laboris nisi ut aliquip exea commodo consequat.Duis aute irure dolor in reprehenderit in voluptate velit esse cillum irure dolor in reprehenderit in voluptate velit esse irure</p>
      <div class="closing">Regards</div>
      <div class="signature" role="img" aria-label="Handwritten signature of Hallworth"></div>
    </section>

    <div class="band band--bottom"></div>
  </main>
</body>
</html>
```